business card design for a plumbing contractor

i need a double business card for a plumbing business, our initial service is residential Sewer Drain Cleaning.

Target Market(s)

other plumbing Business

Industry/Entity Type

Plumbing

Contact Information for Business Card

www.PipeworksCrestline.example- 5817302946-

Font styles to use
Serif

Colors
ec1f27
0455a3

```html
<!DOCTYPE html>
<html lang="en">
<head>
<meta charset="utf-8">
<title>Pipeworks Crestline – Business Card</title>
<link rel="stylesheet" href="https://fonts.googleapis.com/css2?family=Open+Sans:wght@400;600;700&display=swap">
<style>
  :root {
    --brand-red: #ec1f27;
    --brand-blue: #0d5bc0;
    --brand-taupe: #9a8c73;
    --card-white: #ffffff;
    --page-bg: #e6e7e9;
    --text-on-blue: #ffffff;
  }
  * { box-sizing: border-box; margin: 0; padding: 0; }
  html, body {
    width: 1200px;
    height: 977px;
    overflow: hidden;
    background: var(--page-bg);
    font-family: "Open Sans", sans-serif;
  }
  .sheet {
    position: relative;
    width: 1200px;
    height: 977px;
  }
  .card {
    position: absolute;
    left: 250px;
    width: 700px;
    height: 400px;
    background: var(--card-white);
    overflow: hidden;
    box-shadow: 0 2px 10px rgba(0,0,0,0.12);
  }
  .card--front { top: 60px; }
  .card--back { top: 517px; }

  .wordmark {
    display: flex;
    align-items: flex-start;
    gap: 12px;
  }
  .wordmark__name {
    color: var(--brand-taupe);
    font-weight: 700;
    line-height: 0.92;
    letter-spacing: 0.5px;
  }
  .wordmark__line { display: block; }
  .wordmark__line--second { padding-left: 0.9em; }
  .wordmark__mark {
    background: var(--brand-red);
    flex: none;
  }

  .card--front .wordmark {
    position: absolute;
    left: 0; right: 0;
    top: 120px;
    justify-content: center;
  }
  .card--front .wordmark__name { font-size: 52px; }
  .card--front .wordmark__mark { width: 34px; height: 34px; margin-top: 4px; }

  .services {
    position: absolute;
    left: 0; right: 0;
    bottom: 60px;
    text-align: center;
    color: var(--brand-taupe);
    font-size: 12px;
    font-weight: 600;
    letter-spacing: 2px;
    text-transform: uppercase;
  }
  .services__dot { margin: 0 12px; }

  .card__curve {
    position: absolute;
    inset: 0;
    width: 700px;
    height: 400px;
  }
  .contact {
    position: absolute;
    left: 62px;
    top: 122px;
    color: var(--text-on-blue);
  }
  .contact__name { font-size: 24px; font-weight: 700; }
  .contact__title { font-size: 14px; font-weight: 600; margin-top: 2px; }
  .contact__list { list-style: none; margin-top: 24px; }
  .contact__item {
    display: flex;
    align-items: center;
    gap: 14px;
    font-size: 14px;
    line-height: 26px;
  }
  .contact__icon { width: 14px; height: 14px; flex: none; fill: var(--text-on-blue); }

  .card--back .wordmark {
    position: absolute;
    right: 50px;
    top: 128px;
    gap: 8px;
  }
  .card--back .wordmark__name { font-size: 30px; }
  .card--back .wordmark__mark { width: 22px; height: 22px; margin-top: 2px; }
</style>
</head>
<body>
<main class="sheet">

  <section class="card card--front" aria-label="Card front">
    <div class="wordmark">
      <span class="wordmark__name">
        <span class="wordmark__line">Pipeworks</span>
        <span class="wordmark__line wordmark__line--second">Crestline</span>
      </span>
      <span class="wordmark__mark" aria-hidden="true"></span>
    </div>
    <p class="services">
      Sewer Drain Cleaning<span class="services__dot">·</span>Maintenance<span class="services__dot">·</span>Trenchless Pipe Installs
    </p>
  </section>

  <section class="card card--back" aria-label="Card back">
    <svg class="card__curve" viewBox="0 0 700 400" aria-hidden="true">
      <circle cx="40" cy="250" r="380" fill="var(--brand-red)"/>
      <circle cx="40" cy="250" r="369" fill="var(--card-white)"/>
      <circle cx="40" cy="250" r="362" fill="var(--brand-blue)"/>
    </svg>

    <div class="contact">
      <p class="contact__name">Dana Whitfield</p>
      <p class="contact__title">Manager</p>
      <ul class="contact__list">
        <li class="contact__item">
          <svg class="contact__icon" viewBox="0 0 24 24"><path d="M6.6 10.8a15.1 15.1 0 0 0 6.6 6.6l2.2-2.2a1 1 0 0 1 1-.25 11.4 11.4 0 0 0 3.6.57 1 1 0 0 1 1 1V20a1 1 0 0 1-1 1A17 17 0 0 1 3 4a1 1 0 0 1 1-1h3.5a1 1 0 0 1 1 1c0 1.25.2 2.45.57 3.6a1 1 0 0 1-.25 1z"/></svg>
          <span>5817302946</span>
        </li>
        <li class="contact__item">
          <svg class="contact__icon" viewBox="0 0 24 24"><circle cx="12" cy="12" r="10"/></svg>
          <span>www.PipeworksCrestline.example</span>
        </li>
        <li class="contact__item">
          <svg class="contact__icon" viewBox="0 0 24 24"><path d="M2 5h20v14H2z" fill="var(--text-on-blue)"/><path d="M3 6.5l9 7 9-7" fill="none" stroke="var(--brand-blue)" stroke-width="1.6"/></svg>
          <span>Dispatcher@PipeworksCrestline.example</span>
        </li>
      </ul>
    </div>

    <div class="wordmark">
      <span class="wordmark__name">
        <span class="wordmark__line">Pipeworks</span>
        <span class="wordmark__line wordmark__line--second">Crestline</span>
      </span>
      <span class="wordmark__mark" aria-hidden="true"></span>
    </div>
  </section>

</main>
</body>
</html>
```